Flyer for Harbourline Accounting & Taxation, a local tax practice

Flyer for my business to be distributed locally in the Western Suburb of Melbourne (Size: DL, Fold: Flat, Backside: Blank) This will include below information (Font, color and capitalization of the text is for the designer's creativity):
Harbourline Accounting & Taxation Your Local Tax Accountant
ABN: 37 481 259 604
Address: 9 Marlo Place, Wattle Bend
kolvend@hbatx.com.au
Call Tobias on 0419 786 205 to book your appointment
Services we offer:
Individual & Company Tax Returns
Company & Trust formation
Business Advisory
Bookkeeping
BAS & IAS
Payroll
TPAR
Please include the logo of the business attached which was designed by PixelForum few years ago.
Please include the NBF, RCQ and Lumo logos somewhere in the bottom, preferable the same size and aligned (attached)

```html
<!DOCTYPE html>
<html lang="en">
<head>
<meta charset="utf-8">
<title>Harbourline Accounting &amp; Taxation – Flyer</title>
<link rel="stylesheet" href="https://fonts.googleapis.com/css2?family=Open+Sans:wght@400;600;700&family=Roboto+Condensed:wght@700;800&display=swap">
<style>
  :root {
    --orange: #e8701e;
    --ink: #3b3b3d;
    --grey: #5a5a5c;
    --band: #48484a;
    --paper: #ffffff;
  }
  * { box-sizing: border-box; margin: 0; padding: 0; }
  html, body { width: 1200px; height: 2704px; overflow: hidden; background: var(--paper); }
  body { font-family: "Open Sans", Arial, sans-serif; color: var(--ink); }
  .flyer { position: relative; width: 1200px; height: 2704px; background: var(--paper); overflow: hidden; }

  .brand { position: absolute; top: 90px; left: 0; right: 0; display: flex; justify-content: center; align-items: center; gap: 30px; }
  .brand-square { width: 70px; height: 70px; background: var(--ink); }
  .brand-name { font-weight: 600; font-size: 50px; color: var(--ink); line-height: 1.1; }

  .headline { position: absolute; top: 300px; left: 0; right: 0; text-align: center; font-family: "Roboto Condensed", Arial, sans-serif; font-weight: 800; line-height: 1; }
  .headline-name { font-size: 150px; color: var(--orange); letter-spacing: 1px; }
  .headline-sub { font-size: 92px; color: var(--ink); margin-top: 12px; }
  .headline-sub .amp { color: var(--orange); }
  .headline-tag { font-size: 74px; color: var(--orange); margin-top: 14px; }

  .services { position: absolute; top: 760px; left: 110px; right: 80px; display: grid; grid-template-columns: 1fr 0.78fr; column-gap: 40px; }
  .services ul { list-style: none; }
  .services li { position: relative; padding-left: 62px; font-size: 44px; font-weight: 600; color: var(--grey); line-height: 1.15; margin-bottom: 26px; }
  .services li::before { content: ""; position: absolute; left: 0; top: 10px; width: 30px; height: 30px; background: var(--grey); }

  .call { position: absolute; top: 1110px; left: 100px; right: 100px; height: 170px; display: flex; border: 5px solid var(--ink); border-radius: 85px; overflow: hidden; background: var(--paper); }
  .call-number { flex: 0 0 540px; background: var(--orange); color: var(--paper); padding: 18px 0 0 58px; border-radius: 0 85px 85px 0; }
  .call-number .who { font-size: 46px; font-weight: 600; line-height: 1.1; }
  .call-number .phone { font-family: "Roboto Condensed", Arial, sans-serif; font-weight: 800; font-size: 76px; line-height: 1; }
  .call-book { flex: 1; display: flex; flex-direction: column; justify-content: center; padding: 0 70px 0 40px; color: var(--ink); }
  .call-book .lead { font-size: 42px; line-height: 1.1; }
  .call-book .appt { font-family: "Roboto Condensed", Arial, sans-serif; font-weight: 800; font-size: 54px; line-height: 1.05; }

  .photo { position: absolute; top: 1320px; left: 0; right: 0; height: 1000px;
    background: linear-gradient(180deg, #f6f7f9 0%, #e2e6eb 30%, #c3cad2 62%, #9aa3ad 85%, #7e8791 100%); }

  .footer { position: absolute; top: 2320px; left: 0; right: 0; bottom: 0; background: var(--band); border-top: 14px solid var(--orange); color: var(--paper); text-align: center; padding-top: 60px; }
  .abn { display: flex; justify-content: center; align-items: center; gap: 26px; font-size: 50px; font-weight: 700; letter-spacing: 2px; }
  .abn-tag { background: var(--orange); padding: 4px 26px; border-radius: 12px; }
  .address { font-size: 48px; margin-top: 40px; }
  .email { font-size: 48px; margin-top: 22px; }
</style>
</head>
<body>
<main class="flyer">
  <header class="brand">
    <span class="brand-square"></span>
    <span class="brand-name">Harbourline<br>Accounting &amp; Taxation</span>
  </header>

  <section class="headline">
    <div class="headline-name">HARBOURLINE</div>
    <div class="headline-sub">ACCOUNTING <span class="amp">&amp;</span> TAXATION</div>
    <div class="headline-tag">YOUR LOCAL TAX ACCOUNTANT</div>
  </section>

  <section class="services">
    <ul>
      <li>Individual &amp; Company Tax Returns</li>
      <li>Company &amp; Trust formation</li>
      <li>Business Advisory</li>
    </ul>
    <ul>
      <li>Bookkeeping</li>
      <li>BAS &amp; IAS</li>
      <li>Payroll</li>
      <li>TPAR</li>
    </ul>
  </section>

  <section class="call">
    <div class="call-number">
      <div class="who">Call Tobias</div>
      <div class="phone">0419 786 205</div>
    </div>
    <div class="call-book">
      <div class="lead">to book your</div>
      <div class="appt">APPOINTMENT</div>
    </div>
  </section>

  <div class="photo" role="img" aria-label="Photo of an accountant seen from behind working at a desktop computer showing charts and a spreadsheet"></div>

  <footer class="footer">
    <div class="abn"><span class="abn-tag">ABN</span><span>37 481 259 604</span></div>
    <div class="address">9 Marlo Place, Wattle Bend</div>
    <div class="email">kolvend@hbatx.com.au</div>
  </footer>
</main>
</body>
</html>
```